Snapvella needs You

Help us create an inviting, amazing, sleek, simple, clear landing page for a picture-memory-social connection site!

Business Name: SnapVella
Industry: Social Networking and Creativity through Pictures
A web platform for and about a community that is driven by a passion for sharing, caring, bonding, collaborating, creating and earning with pictures, through pictures and other related creative activities. This is going to be a great site for all creative artists-photographers, artists, graphic artists to express their work and their creativity.

The main focus of the site is - CONNECTIONS.
This will be uncoded.

Desired Website Screen Size
1024x768... Widescreen/Landscape orientation, is what we mean... So it fits on a CPU screen.

Desired look and feel and message
Look: Visitor should feel immersed in the page, in the world the page creates, simple, elegant, sophisticated, contemporary. We really like a clean uncluttered look.

Special mention: By the way we love the marketing genius who thought up this branding for pralu yogurt where they used the two dots above the o to create a branding effect that made this brand instantly identifiable. http://www.pralu.ca/en/

The two dots by themselves without having even the name present brings up the whole brand now. The dots are used above all the ingredients of the yogurt creating friendly figures, and above people in commercials-bringing the people onto the side of "team" pralu. Snapvella may have a character created or something distinctive in the letters in the name created to brand the site as well.

Feel: Engaging; Magical without being corny, here is a link to give an example look and feel but please do not be hindered in your creativity by this suggestion. We love all creative angles.
http://artscrapbin.com/graphic/5830261-camera-film-roll-blue-background

Message: Life and memories and connections through pictures.

Target audience:
The site is focused on pictures but not confined to photography enthusiasts (although they are an integral part of the site). Customers/Visitors will include families, corporates and the younger generation - all age groups, all class, everyone with pictures to express, memories to share.

Website design we like:
http://varnomdesign.com/work/northern-choral-guild/
http://varnomdesign.com/work/bitsprout/

What colors do we want to see on our landing page?
We would like the background to be grey or blue since it is grey is picture neutral colour and blue highlights pictures well and we also like blue and silver, which can be integrated into the theme. Also like green. But please do not let these instructions limit your creativity. We are open to new ideas and colours.

Predetermined Concepts if any:
We have a concept in mind and we think it would be cool to have an interface for the user through the back of a camera on the landing page -This could be used to create a scene or world the visitor feels a part of or is immersed into. The back screen of the camera may act as a screen for the slideshow of featured pictures on the site.

Content on the Page:
Photo Gallery with full screen, thumbnail view, zoom option etc.
Prominent but short introductory message
Sign in / Login Options
Links: Home Page; About; Info/Help; Contact Us; Privacy Policy; Terms of Use
At the bottom of the page: Follow Me/Like/Workmesh...social buttons.

Please feel free to add any other element to the landing page that you think might add to the effect of simple yet amazing look -clean, simple, uncluttered, sophisticated, stylish, inviting and engaging.
The concept is a guideline, but we would like you to be as creative as you can, even if it meant stepping out of these guidelines - rethink design, style, content if you like. We believe in bringing a solution in an innovative yet simple and elegant style. Something a visitor would be intrigued enough to explore and the guest would feel comfortable enough taking that step forward to have fun on the site. If you believe in the same, and you have the skill then you will have what we need. Good luck, go for it and we are excited to see what the amazing designers on this amazing site have to offer.
If you have any questions please free to ask.
Updates

HI wanted to send an update that this project design has been guaranteed.

Our site will be one to celebrate and showcase imagination as well as connection.  We would love to see what you create. Keep in mind our site will showcase all creativity, photographs, artists, graphic artists so this would be a benefit you may want to take advantage of in the future, a place where, if you so choose, you could gain exposure for your work. Therefore, even if you do not win the design project there is possible future benefit.

Imagination is everything.
Imagination encircles the world.-Holberg

Reason: We are giving the designers who accepted invites but have not yet submitted a chance to finish their submissions and the ones who are working on revisions a chance to finish those:)

Hello everyone,

Due to time constraints we must come to a decision sooner than the deadline of 28th. 

So, please try to submit any new designs or modifications to the old ones before the 26th. We are very thankful to all of you who have participated - for your designs, enthusiasm and kind words. 

Good luck! :)

• Thank you for the interest shown and your submissions! Designers who have submitted up until now have shown great potential. We are VERY excited with the quality of work and designs.

We want to add that Snapvella is not exclusively for the photographers. The site is for every person who may have a picture to store, organise, use or share - whether publicly or with only a few friends and family.

Snapvella is about allowing people to take control of their creativity. It is about providing tools to our users so that they can build their own connections and social network... of friends, family, fans, clients, ideas, thoughts, emotions etc. through pictures without worrying about their privacy or control over their creations.

With this update we want to encourage others to go beyond the camera theme. Do not let us restrict your creativity. Let YOUR OWN ideas take over if that’s what you think will best convey the message and will appeal to the users.

```html
<!DOCTYPE html>
<html lang="en">
<head>
<meta charset="utf-8">
<title>SnapVella — Life, memories &amp; connections through pictures</title>
<link href="https://fonts.googleapis.com/css2?family=Lobster&family=Pacifico&family=Arimo:wght@400;700&display=swap" rel="stylesheet">
<style>
  :root {
    --wood-light: #f3d9a6;
    --wood-mid: #e9c48a;
    --wood-dark: #dcb27a;
    --brand-blue: #2f78a8;
    --band-blue: #3585b5;
    --white: #ffffff;
    --gold-light: #f2cf5e;
    --gold-dark: #c99a1e;
    --gold-text: #5a3d05;
    --tagline: #a0720f;
    --frame: #fbfbf8;
    --footer-bg: #e8e8e6;
    --footer-line: #5d6a72;
    --footer-text: #444444;
    --social: #3d6f9e;
  }
  * { box-sizing: border-box; margin: 0; padding: 0; }
  html, body { width: 1200px; height: 900px; overflow: hidden; }
  body {
    position: relative;
    font-family: "Arimo", Arial, sans-serif;
    background: linear-gradient(90deg, var(--wood-mid) 0%, var(--wood-light) 30%, var(--wood-mid) 55%, var(--wood-light) 80%, var(--wood-dark) 100%);
  }
  .wood-surface { position: absolute; inset: 0 0 255px 0; }

  .brand {
    position: absolute; left: 42px; top: 0; width: 187px; height: 115px;
    background: linear-gradient(180deg, #3a87b8, var(--brand-blue));
    box-shadow: 0 3px 6px rgba(0,0,0,.3);
    display: flex; flex-direction: column; align-items: center; justify-content: flex-end;
    padding-bottom: 12px; gap: 8px;
  }
  .brand-mark { width: 30px; height: 30px; background: var(--white); }
  .brand-name { font-family: "Pacifico", cursive; font-size: 30px; line-height: 1; color: var(--white); }

  .main-nav { position: absolute; top: 58px; left: 455px; display: flex; gap: 0; }
  .main-nav a {
    color: var(--white); text-decoration: none; font-weight: 700; font-size: 14px;
    margin-right: 38px; text-shadow: 0 1px 1px rgba(0,0,0,.2);
  }
  .account { position: absolute; top: 54px; left: 824px; display: flex; gap: 16px; }
  .account a {
    display: flex; align-items: center; justify-content: center;
    width: 89px; height: 31px; border-radius: 14px;
    background: linear-gradient(180deg, var(--gold-light), var(--gold-dark));
    border: 1px solid #a47a12;
    font-family: "Pacifico", cursive; font-size: 16px; color: var(--white);
    text-decoration: none; text-shadow: 0 1px 1px rgba(0,0,0,.35);
  }

  .showcase {
    position: absolute; left: 197px; top: 144px; width: 817px; height: 440px;
    background: var(--frame); box-shadow: 0 2px 6px rgba(0,0,0,.25);
  }
  .showcase-photo {
    position: absolute; left: 28px; top: 27px; width: 759px; height: 387px;
    background: linear-gradient(180deg, #1d2a45 0%, #33365a 45%, #a4452b 62%, #3b2b24 75%, #0f1216 100%);
  }
  .slide-dots { position: absolute; left: 0; right: 0; bottom: 7px; display: flex; justify-content: center; gap: 9px; }
  .slide-dots span { width: 11px; height: 11px; border-radius: 50%; background: #cfcfcf; border: 1px solid #9a9a9a; }

  .tagline {
    position: absolute; top: 598px; left: 0; width: 1190px; text-align: center;
    font-family: "Lobster", cursive; font-size: 23px; color: var(--tagline);
  }

  .info-band {
    position: absolute; left: 0; top: 645px; width: 1200px; height: 196px;
    background: var(--band-blue);
  }
  .info-block { position: absolute; top: 26px; width: 405px; color: var(--white); }
  .info-block.about { left: 59px; }
  .info-block.connect { left: 746px; }
  .info-block h2 { font-family: "Pacifico", cursive; font-weight: 400; font-size: 23px; line-height: 1.2; margin-bottom: 12px; }
  .info-block p { font-size: 14px; line-height: 17.5px; }
  .network-art {
    position: absolute; left: 512px; top: 17px; width: 165px; height: 165px;
    background: radial-gradient(circle, #2b6f9c 0%, var(--band-blue) 70%);
  }

  .site-footer {
    position: absolute; left: 0; top: 841px; width: 1200px; height: 59px;
    background: var(--footer-bg); border-top: 3px solid var(--footer-line);
    font-size: 12px; color: var(--footer-text);
  }
  .copyright { position: absolute; left: 29px; top: 24px; }
  .legal { position: absolute; left: 292px; top: 24px; display: flex; gap: 12px; }
  .legal a { color: var(--footer-text); text-decoration: none; }
  .social { position: absolute; right: 16px; top: 20px; display: flex; gap: 12px; }
  .social a { display: flex; align-items: center; gap: 5px; color: var(--social); text-decoration: none; font-weight: 700; font-size: 12px; }
  .social a span { width: 14px; height: 14px; border-radius: 50%; background: var(--social); }
</style>
</head>
<body>
  <div class="wood-surface" role="img" aria-label="Light wooden plank texture background"></div>

  <header>
    <a class="brand" href="#">
      <span class="brand-mark"></span>
      <span class="brand-name">SnapVella</span>
    </a>
    <nav class="main-nav">
      <a href="#">Home</a>
      <a href="#">About Us</a>
      <a href="#">Info</a>
      <a href="#">Contact Us</a>
    </nav>
    <div class="account">
      <a href="#">Log in</a>
      <a href="#">Sign Up</a>
    </div>
  </header>

  <section class="showcase">
    <div class="showcase-photo" role="img" aria-label="Featured photo: a lit city bridge with twin towers over a river at dusk"></div>
    <div class="slide-dots"><span></span><span></span><span></span><span></span></div>
  </section>

  <p class="tagline">Life, memories &amp; connections through pictures</p>

  <section class="info-band">
    <div class="info-block about">
      <h2>About SnapVella</h2>
      <p>Lorem ipsum dolor sit amet, consectetur adipiscing elit. Aliquam accumsan sagittis velit. Fusce a augue nisl. Cras scelerisque porttitor arcu, at malesuada nulla rutrum sed. Curabitur quis massa massa, at auctor nunc. Phasellus pellentesque aliquam libero vel tincidunt. Integer id dolor id elit elementum rhoncus.</p>
    </div>
    <div class="network-art" role="img" aria-label="Illustration of picture frames linked together as a network"></div>
    <div class="info-block connect">
      <h2>Get Connected</h2>
      <p>Lorem ipsum dolor sit amet, consectetur adipiscing elit. Aliquam accumsan sagittis velit. Fusce a augue nisl. Cras scelerisque porttitor arcu, at malesuada nulla rutrum sed. Curabitur quis massa massa, at auctor nunc. Phasellus pellentesque aliquam libero vel tincidunt. Integer id dolor id elit elementum rhoncus.</p>
    </div>
  </section>

  <footer class="site-footer">
    <p class="copyright">© 2012 SnapVella All Rights Reserved</p>
    <nav class="legal">
      <a href="#">Privacy Policy</a>
      <a href="#">Terms &amp; Conditions</a>
    </nav>
    <nav class="social">
      <a href="#"><span></span>Circlio</a>
      <a href="#"><span></span>Chirply</a>
      <a href="#"><span></span>Workmesh</a>
      <a href="#"><span></span>Blogstack</a>
    </nav>
  </footer>
</body>
</html>
```